Cause bitches need love too!

I am creating an ad campaign. It will be a series of featured dogs in our shelter and they will contain a picture of the dog wich should be big enough to see on a yard sign and will change every week. I am placing the signs so that they lead you to the shelter. This is why I am also including the copy that says "you're almost there".

I have 4 tag lines:

1. Find unconditional Love.
2. She'll Love you furever!
3. He'll always listen.
4. Meet your new BFF

You're almost there 217 W Marlowe Ave
Open 10 - 7/Tues-Sat

The dimensions for the sign are 24" wide and 18" high

Every week we will have a different picture of a different dog (hopefully last week's dog gets adopted). Anyhow, I am printing out yard signs, meaning that instead of printing 160 different signs it would be ideal just to replace the photo. So far the copy that is permanent is: "You're almost there. 217 W. Marlowe Ave."

I could silhouette the image of the dog as well and super impose it on the sign, that's also a consideration, but ideally if I could have 4 tag lines I could print 40 signs of each and just replace the photo manually each week from my printer that would save costs.
Updates

Not enough designs to chose from and I edited the brief and committed to pay no matter what to increase the amount of designs as per your suggestions.

Target Market(s)

Animal lovers

Industry/Entity Type

Campaign

Font styles to use
Sans Serif

Colors

Designer to choose colors to be used in the design.

Requirements
Must have
• The dimensions for the sign are 24" wide and 18" high
Nice to have
• I want the signs to be hip, they should have a positive feel to them. You can alter the photos if you like. I am even open to new copy if you think something else works better.

```html
<!DOCTYPE html>
<html lang="en">
<head>
<meta charset="utf-8">
<title>He'll Always Listen – Shelter Yard Sign</title>
<link rel="stylesheet" href="https://fonts.googleapis.com/css2?family=Open+Sans:wght@300;700;800&display=swap">
<style>
  :root {
    --stage: #9a9a9a;
    --sign-top: #dcd7d3;
    --sign-bottom: #b9b2ad;
    --band: #ffffff;
    --ink: #111111;
    --headline: #ffffff;
    --extrude: #1a1a1a;
    --dog-light: #c99a5c;
    --dog-mid: #9a6a34;
    --dog-dark: #3a2a1c;
  }
  * { margin: 0; padding: 0; box-sizing: border-box; }
  html, body {
    width: 800px;
    height: 1200px;
    overflow: hidden;
    background: var(--stage);
    font-family: "Open Sans", Arial, sans-serif;
  }
  .yard-sign {
    position: absolute;
    left: 80px;
    top: 360px;
    width: 640px;
    height: 480px;
    overflow: hidden;
    background: linear-gradient(180deg, var(--sign-top), var(--sign-bottom));
    box-shadow: 0 26px 22px -14px rgba(0,0,0,0.45);
  }
  .dog-photo {
    position: absolute;
    left: 0;
    top: 0;
    width: 272px;
    height: 366px;
    background: radial-gradient(ellipse at 55% 40%, var(--dog-light) 0%, var(--dog-mid) 55%, var(--dog-dark) 100%);
    border-radius: 0 40% 0 0 / 0 30% 0 0;
  }
  .tagline {
    position: absolute;
    right: 18px;
    color: var(--headline);
    font-weight: 800;
    line-height: 1;
    text-align: right;
    white-space: nowrap;
    letter-spacing: -0.04em;
    text-shadow:
      -1px 1px 0 var(--extrude),
      -2px 2px 0 var(--extrude),
      -3px 3px 0 var(--extrude),
      -4px 3px 0 var(--extrude),
      -5px 4px 0 var(--extrude);
  }
  .tagline--he { top: 90px;  font-size: 105px; }
  .tagline--always { top: 176px; font-size: 98px; }
  .tagline--listen { top: 239px; font-size: 140px; }
  .info-band {
    position: absolute;
    left: 0;
    top: 366px;
    width: 100%;
    height: 114px;
    background: var(--band);
  }
  .address, .hours {
    position: absolute;
    left: 0;
    width: 100%;
    text-align: center;
    line-height: 1;
    color: var(--ink);
    white-space: nowrap;
  }
  .address { top: 20px; font-size: 40px; font-weight: 800; letter-spacing: 0.01em; }
  .hours { top: 67px; font-size: 31px; font-weight: 300; }
</style>
</head>
<body>
  <main class="yard-sign">
    <div class="dog-photo" role="img" aria-label="Photo of the featured shelter dog, a tan and black shepherd mix tilting its head"></div>
    <h1>
      <span class="tagline tagline--he">HE'LL</span>
      <span class="tagline tagline--always">ALWAYS</span>
      <span class="tagline tagline--listen">LISTEN</span>
    </h1>
    <footer class="info-band">
      <p class="address">217 W MARLOWE AVE</p>
      <p class="hours">OPEN TUESDAY-SUNDAY TILL 7PM</p>
    </footer>
  </main>
</body>
</html>
```